Play on Words (French Puns)

Cover (11 x 17.8 cm) for a book of French plays on words. (Author: "Mathis Lobry" Title: "The Tricksters" Subtitle "Verbal Treats To Nibble" Publisher (at the bottom of the page): "Quill Press"

Target Market(s)

General public

Industry/Entity Type

Book Publisher

Colors

Designer to choose colors to be used in the design.

Requirements
Must have
• "Unserious" look
Should not have
• Eiffel Tower, triumphal arch (it's a book on French language, not on France)

```html
<!DOCTYPE html>
<html lang="en">
<head>
<meta charset="utf-8">
<title>The Tricksters – Mathis Lobry</title>
<link rel="stylesheet" href="https://fonts.googleapis.com/css2?family=Fira+Sans:wght@800&family=Nunito:wght@900&family=Open+Sans:wght@300&display=swap">
<style>
  :root {
    --paper: #ffffff;
    --ink: #0a0a0a;
    --teal: #0e9aa7;
    --green: #86c23a;
    --coral: #ee5747;
    --shadow: rgba(0, 0, 0, 0.18);
  }
  html, body {
    margin: 0;
    padding: 0;
    overflow: hidden;
    background: var(--paper);
  }
  .cover {
    position: relative;
    width: 840px;
    height: 1200px;
    background: var(--paper);
    overflow: hidden;
  }
  .author {
    position: absolute;
    left: 31px;
    top: 86px;
    margin: 0;
    font-family: "Fira Sans", sans-serif;
    font-weight: 800;
    font-size: 50px;
    line-height: 1;
    color: var(--ink);
  }
  .title {
    position: absolute;
    left: 0;
    top: 270px;
    width: 840px;
    height: 360px;
  }
  .title text {
    font-family: "Nunito", sans-serif;
    font-weight: 900;
    font-size: 156px;
  }
  .title .teal { fill: var(--teal); }
  .title .green { fill: var(--green); }
  .title .coral { fill: var(--coral); }
  .subtitle {
    position: absolute;
    left: 31px;
    top: 694px;
    margin: 0;
    font-family: "Fira Sans", sans-serif;
    font-weight: 800;
    font-size: 29px;
    line-height: 1;
    color: var(--ink);
  }
  .publisher {
    position: absolute;
    left: 0;
    width: 840px;
    top: 1116px;
    margin: 0;
    text-align: center;
    font-family: "Open Sans", sans-serif;
    font-weight: 300;
    font-size: 22px;
    line-height: 1;
    color: var(--ink);
  }
</style>
</head>
<body>
  <main class="cover">
    <p class="author">Mathis Lobry</p>

    <svg class="title" viewBox="0 0 840 360" role="img" aria-label="The Tricksters">
      <defs>
        <filter id="lift" x="-5%" y="-5%" width="110%" height="115%">
          <feDropShadow dx="2" dy="3" stdDeviation="2" flood-color="var(--shadow)"/>
        </filter>
      </defs>
      <g filter="url(#lift)">
        <text x="32" y="146">
          <tspan class="green">T</tspan><tspan class="teal">H</tspan><tspan class="coral">E</tspan>
        </text>
        <text x="32" y="330" textLength="776" lengthAdjust="spacingAndGlyphs">
          <tspan class="coral">T</tspan><tspan class="teal">R</tspan><tspan class="teal">I</tspan><tspan class="coral">C</tspan><tspan class="teal">K</tspan><tspan class="green">S</tspan><tspan class="teal">T</tspan><tspan class="teal">E</tspan><tspan class="coral">R</tspan><tspan class="teal">S</tspan>
        </text>
      </g>
    </svg>

    <p class="subtitle">Verbal Treats To Nibble</p>

    <p class="publisher">Quill Press</p>
  </main>
</body>
</html>
```